NEW Website DESIGN for Glass & Solid Surfaces Company

Brand New website, contemporary, clean, visual (images), not busy. ATTACHED IS OUR LOG THAT YOU MUST USE.

The company is called Brightwell Panes & Stoneworks (BrightwellPS)
www.brightwellps.com
The website should be www.brightwellpns.com
one page for glass one page for solid surfaces www.brightwellpanesplashes.co.uk
www.brightwellstoneworkss.co.uk

Target Market(s)

Hotels, Commercial projects, Small focus on residential

Industry/Entity Type

Construction

Number of Pages Required

5+ page

Font styles to use
Sans Serif

Requirements
Must have
• COLOURS AS PER OUR LOGO - WHITE/YELLOW/GREY - WHITE BACK GROUND
• CLEAR SIMPLE NAVIGATION - MODER CLEAN CUT - DESIGN FEEL
• LATEST NAVIGATION FOR IMAGES and text to include per project details
• WORK/PROJECT AREA - NEWS AREA - TEAM AREA/ABOUT US/CONTACT US
• NEW PAGEwww.brightwellpanesplashes.co.uk - NEW PAGE www.brightwellstoneworkss.co.uk
• PLEASE COPY THIS TYPE OF TEMPALTE
• https://www.harlowmead.co.uk/project/grand-halls/
• MOBILE READY
• WORDPRESS
• MODERN IMAGES INCLUDING VELMARA KESTRIN AND GLASS PROJECTS
Nice to have
• NEW DESIGN MODER FRESH
• WEBSITES I LIKE THE TEMPLATE SHOULD BE LIKE THE WEBSITE BELOW
• https://www.harlowmead.co.uk/
Should not have
• NOT Old fashion template, not busy NAVIGATION
• NO BLACK
• NO DARK GREYS
• NOT LOTS OF YELLOW
• RESDENTIAL IMAGES

```html
<!DOCTYPE html>
<html lang="en">
<head>
<meta charset="utf-8">
<title>Brightwell Panes &amp; Stoneworks</title>
<link href="https://fonts.googleapis.com/css2?family=Open+Sans:wght@400;600;700&family=Oswald:wght@400;500&display=swap" rel="stylesheet">
<style>
:root{
  --yellow:#f3e600;
  --band:#efefef;
  --text:#6b6b6b;
  --title:#5a5a5a;
  --line:#e2e2e2;
  --white:#ffffff;
  --footer:#4d4d4d;
  --badge-ring:#8a8a8a;
  --badge-accent:#e0732c;
}
*{box-sizing:border-box;margin:0;padding:0}
html,body{width:1200px;height:4800px;overflow:hidden;background:var(--white)}
body{position:relative;font-family:"Open Sans",Arial,sans-serif;color:var(--text)}
.abs{position:absolute}
.section-title{position:absolute;left:0;width:1200px;text-align:center;font-size:24px;font-weight:600;color:var(--title)}
.section-title::before{content:"";position:absolute;left:565px;top:-14px;width:70px;height:3px;background:var(--yellow)}
.section-sub{position:absolute;left:0;width:1200px;text-align:center;font-size:15px;color:var(--text)}
.band{position:absolute;left:38px;width:1124px;background:var(--band)}
.photo{position:absolute;overflow:hidden}
.btn-yellow{position:absolute;background:var(--yellow);color:#555;font-size:13px;font-weight:700;letter-spacing:1px;display:flex;align-items:center;justify-content:center;gap:14px}

/* header */
.brand-curve{position:absolute;left:-60px;top:-120px;width:400px;height:310px;border-radius:50%;background:var(--white);z-index:3}
.brand{position:absolute;left:40px;top:14px;z-index:4;text-align:center;width:240px}
.brand-mark{width:96px;height:96px;border-radius:50%;background:#8d8d8d;margin:0 auto 8px}
.brand-name{font-size:14px;font-weight:600;color:#555;white-space:nowrap}
.nav{position:absolute;left:432px;top:48px;display:flex;height:40px;align-items:center}
.nav a{font-size:13px;font-weight:600;color:#555;text-decoration:none;padding:0 18px;height:40px;display:flex;align-items:center;border-right:1px solid var(--line)}
.nav a:last-child{border-right:none}
.nav a.active{background:var(--yellow)}
.hero{left:38px;top:144px;width:1124px;height:534px;
  background:
    linear-gradient(180deg,rgba(0,0,0,0) 55%,rgba(0,0,0,.35) 100%),
    radial-gradient(ellipse 30% 40% at 88% 22%,rgba(245,205,120,.85),rgba(245,205,120,0) 70%),
    radial-gradient(ellipse 25% 55% at 58% 42%,rgba(250,238,205,.9),rgba(250,238,205,0) 70%),
    linear-gradient(100deg,#5b5148 0%,#8c8170 18%,#cdbf9c 36%,#e9e2cf 50%,#b7a988 64%,#6d655a 82%,#3f3a35 100%)}
.hero-title{position:absolute;left:38px;top:550px;width:1124px;text-align:center;font-family:"Oswald",Arial,sans-serif;font-size:38px;line-height:44px;color:var(--white);text-transform:uppercase;z-index:2;text-shadow:0 2px 6px rgba(0,0,0,.4)}

/* approval + stats */
.badge{left:140px;top:758px;width:200px;height:200px}
.stats{left:388px;top:788px;width:672px;height:140px;border:2px solid var(--line);display:flex;padding:10px 6px}
.stat{flex:1;padding:6px 12px;border-right:1px solid var(--line);white-space:nowrap}
.stat:last-child{border-right:none}
.stat svg{display:block;margin-bottom:14px}
.stat b{display:block;font-size:13px;font-weight:600;color:#888}
.stat span{font-size:16px;font-weight:600;color:#777}

/* clients */
.clients{display:flex;gap:17px;position:absolute;left:174px;top:1158px}
.client{width:124px;height:64px;background:var(--white);display:flex;align-items:center;justify-content:center;font-size:13px;font-weight:600;color:#8a7b3a}
.pager{position:absolute;top:1243px;width:30px;height:30px;display:flex;align-items:center;justify-content:center}

/* services */
.service-card{position:absolute;top:1798px;width:438px;height:122px;background:var(--white);box-shadow:0 6px 16px rgba(0,0,0,.16);text-align:center;padding-top:32px}
.service-card h3{font-size:24px;font-weight:600;color:#555}
.service-card p{font-size:12px;font-weight:700;color:var(--yellow);letter-spacing:.5px}

/* testimonials */
.quote{position:absolute;top:3078px;width:300px;height:230px}
.quote p{position:absolute;left:62px;top:46px;width:178px;font-size:12px;line-height:18px;text-align:center;color:#555}
.quote .mark{position:absolute;font-size:70px;font-weight:700;color:var(--yellow);line-height:1}
.client-name{position:absolute;top:3300px;width:300px;display:flex;justify-content:center;align-items:center;gap:8px;font-size:18px;font-weight:700;color:#333}
.client-name i{width:14px;height:14px;border-radius:50%;background:#333;display:block}

/* news */
.news{position:absolute;top:3562px;width:290px;height:262px}
.news-text{position:absolute;left:12px;top:164px;width:266px;color:var(--white);font-size:12px;line-height:17px}
.news-text b{display:block;color:var(--yellow);font-size:11px;margin-top:8px;letter-spacing:.5px}

/* contact */
.contact-box{position:absolute;top:4496px;width:294px;height:182px;border:2px solid var(--line);text-align:center;padding-top:38px}
.contact-box h4{font-size:16px;font-weight:700;color:#555;margin-top:10px}
.contact-box p{font-size:13px;color:#666;margin-top:4px}

/* footer */
.footer{left:0;top:4762px;width:1200px;height:38px;background:var(--footer);color:#ddd;font-size:11px;display:flex;align-items:center;padding:0 142px;justify-content:space-between}
.footer .dots{display:flex;gap:14px}
.footer .dots i{width:9px;height:9px;border-radius:50%;background:#ddd;display:block}
</style>
</head>
<body>

<!-- Header -->
<div class="brand-curve"></div>
<div class="brand">
  <div class="brand-mark"></div>
  <div class="brand-name">Brightwell Panes &amp; Stoneworks</div>
</div>
<nav class="nav">
  <a class="active">Home</a><a>About Us</a><a>Glass</a><a>Solid Surfaces</a><a>Projects</a><a>News</a><a>Contact Us</a>
</nav>
<div class="photo hero" role="img" aria-label="Hotel lobby interior with glass screens and reception desk"></div>
<div class="hero-title">Hotel and commercial project fit out<br>refurbishment specialists</div>

<!-- Approval and stats -->
<svg class="abs badge" viewBox="0 0 200 200" role="img" aria-label="Approved supplier badge">
  <circle cx="100" cy="100" r="94" fill="#fff" stroke="#8a8a8a" stroke-width="8"/>
  <circle cx="100" cy="100" r="80" fill="none" stroke="#cfcfcf" stroke-width="2"/>
  <rect x="62" y="56" width="76" height="30" rx="4" fill="#e0732c"/>
  <rect x="50" y="100" width="100" height="10" rx="5" fill="#9a9a9a"/>
  <rect x="56" y="122" width="88" height="18" rx="4" fill="#7a7a7a"/>
</svg>
<div class="abs stats">
  <div class="stat"><svg width="40" height="38" viewBox="0 0 40 40"><rect x="4" y="18" width="32" height="12" rx="3" fill="none" stroke="#f3e600" stroke-width="3"/><path d="M8 18V6h8" fill="none" stroke="#f3e600" stroke-width="3"/><path d="M10 30v5M30 30v5" stroke="#f3e600" stroke-width="3"/></svg><b>3000</b><span>Bathroom</span></div>
  <div class="stat"><svg width="40" height="38" viewBox="0 0 40 40"><rect x="8" y="4" width="24" height="32" fill="none" stroke="#f3e600" stroke-width="3"/><path d="M14 11h4M22 11h4M14 18h4M22 18h4M14 25h4M22 25h4" stroke="#f3e600" stroke-width="3"/></svg><b>50</b><span>Hotels</span></div>
  <div class="stat"><svg width="40" height="38" viewBox="0 0 40 40"><rect x="4" y="16" width="32" height="14" fill="none" stroke="#f3e600" stroke-width="3"/><path d="M10 16V8h20v8M8 30v5M32 30v5" fill="none" stroke="#f3e600" stroke-width="3"/></svg><b>30</b><span>Lobbys</span></div>
  <div class="stat"><svg width="40" height="38" viewBox="0 0 40 40"><path d="M12 30V6h6M26 30V6h6M12 14h14M12 22h14" fill="none" stroke="#f3e600" stroke-width="3"/><path d="M2 34q5-4 9 0t9 0t9 0t9 0" fill="none" stroke="#f3e600" stroke-width="3"/></svg><b>50</b><span>Pools &amp; Spas</span></div>
  <div class="stat"><svg width="40" height="38" viewBox="0 0 40 40"><path d="M4 20L20 6l16 14M9 16v18h22V16" fill="none" stroke="#f3e600" stroke-width="3"/><path d="M20 20v10M15 25h10" stroke="#f3e600" stroke-width="3"/></svg><b>10</b><span>Care Homes</span></div>
</div>

<!-- Clients -->
<div class="band" style="top:1034px;height:291px"></div>
<div class="section-title" style="top:1106px">Our Clients</div>
<div class="clients">
  <div class="client">Larkmoor</div>
  <div class="client">Fenwick Stay</div>
  <div class="client">Orla House</div>
  <div class="client">Veltora</div>
  <div class="client">Grand Marlow</div>
  <div class="client">Sunvale</div>
</div>
<div class="pager" style="left:560px;background:var(--white)"><svg width="10" height="12"><path d="M7 1L2 6l5 5" fill="none" stroke="#777" stroke-width="2"/></svg></div>
<div class="pager" style="left:604px;background:var(--yellow)"><svg width="10" height="12"><path d="M3 1l5 5-5 5" fill="none" stroke="#555" stroke-width="2"/></svg></div>

<!-- Services -->
<div class="section-title" style="top:1438px">Explore Our Main Services</div>
<div class="section-sub" style="top:1480px;text-transform:uppercase;font-size:14px">Harbourline preferred supplier for glass &amp; solid surfaces</div>
<div class="photo" style="left:141px;top:1523px;width:438px;height:263px;background:linear-gradient(180deg,#b8844c 0%,#d8b07c 16%,#eef2f4 30%,#a9c7dc 48%,#dfe6ea 60%,#f4f2ee 78%,#c9c6c0 100%)" role="img" aria-label="Bright commercial interior with glass walls and polished floor"></div>
<div class="photo" style="left:618px;top:1523px;width:438px;height:263px;background:linear-gradient(180deg,#f1efea 0%,#d7d3cb 22%,#6f6a63 42%,#9c968c 58%,#f3f2ef 74%,#d9d6d0 100%)" role="img" aria-label="Reception area with solid surface counter"></div>
<div class="service-card" style="left:141px"><h3>Glass</h3><p>READ MORE</p></div>
<div class="service-card" style="left:618px"><h3>Solid Surfaces</h3><p>READ MORE</p></div>

<!-- Projects -->
<div class="band" style="top:2010px;height:912px"></div>
<div class="section-title" style="top:2108px">Our Projects</div>
<div class="section-sub" style="top:2153px">30 Hotels, 3000 Rooms</div>
<div class="photo" style="left:141px;top:2195px;width:294px;height:215px;background:linear-gradient(180deg,#6e5a44 0%,#b9a37f 30%,#efe9df 55%,#d9cbb4 75%,#8c7355 100%)" role="img" aria-label="Hotel bedroom"></div>
<div class="photo" style="left:141px;top:2430px;width:294px;height:328px;background:linear-gradient(180deg,#f2ead2 0%,#d9c18c 30%,#c8a86a 55%,#efe2c2 78%,#b9995c 100%)" role="img" aria-label="Marble hotel lobby with columns"></div>
<div class="photo" style="left:454px;top:2195px;width:291px;height:263px;background:linear-gradient(180deg,#1f2a44 0%,#3b4f78 35%,#6e84a8 55%,#2e6f96 75%,#1d4d6e 100%)" role="img" aria-label="Rooftop pool at dusk"></div>
<div class="abs" style="left:585px;top:2310px;width:34px;height:34px;background:var(--yellow);display:flex;align-items:center;justify-content:center"><svg width="18" height="18" viewBox="0 0 18 18"><circle cx="7" cy="7" r="5" fill="none" stroke="#555" stroke-width="2"/><path d="M11 11l5 5" stroke="#555" stroke-width="2"/></svg></div>
<div class="photo" style="left:454px;top:2475px;width:291px;height:283px;background:linear-gradient(180deg,#c9cdd1 0%,#eef0f1 35%,#ffffff 55%,#dfe2e4 80%,#b6bbc0 100%)" role="img" aria-label="White hotel bathroom"></div>
<div class="photo" style="left:765px;top:2195px;width:294px;height:215px;background:linear-gradient(180deg,#3f8fd0 0%,#8cc1e4 28%,#2f5a3a 45%,#29a7c4 62%,#5fc7d8 78%,#cdb48c 100%)" role="img" aria-label="Outdoor pool with palm trees and parasols"></div>
<div class="photo" style="left:765px;top:2430px;width:294px;height:328px;background:linear-gradient(180deg,#f4f7fc 0%,#cfdcf2 30%,#9fb6e0 55%,#e5ecf8 80%,#bccbe8 100%)" role="img" aria-label="Clean white care home corridor"></div>
<div class="btn-yellow" style="left:512px;top:2794px;width:173px;height:48px">VIEW ALL <svg width="30" height="10"><path d="M0 5h27M22 1l5 4-5 4" fill="none" stroke="#555" stroke-width="1.6"/></svg></div>

<!-- Testimonials -->
<div class="section-title" style="top:3026px">Client Testimonials</div>
<svg class="abs" style="left:0;top:3078px" width="1200" height="240" viewBox="0 0 1200 240">
  <g fill="none" stroke="#f3e600" stroke-width="3">
    <ellipse cx="290" cy="100" rx="140" ry="95"/><path d="M250 190l-10 40 40-38"/>
    <ellipse cx="600" cy="100" rx="140" ry="95"/><path d="M560 190l-10 40 40-38"/>
    <ellipse cx="914" cy="100" rx="140" ry="95"/><path d="M874 190l-10 40 40-38"/>
  </g>
</svg>
<div class="quote" style="left:140px"><span class="mark" style="left:-4px;top:8px">“</span><p>Clear glass screens fitted on time, with a clean finish in every room and lobby of our new hotel wing.</p><span class="mark" style="left:262px;top:118px">”</span></div>
<div class="quote" style="left:450px"><span class="mark" style="left:-4px;top:8px">“</span><p>Solid surface vanities look smart and wipe clean. The team kept the site tidy and the work ran to plan.</p><span class="mark" style="left:262px;top:118px">”</span></div>
<div class="quote" style="left:764px"><span class="mark" style="left:-4px;top:8px">“</span><p>Great care on our spa refit. Splashbacks and counters were cut well and fitted with very little fuss.</p><span class="mark" style="left:262px;top:118px">”</span></div>
<div class="client-name" style="left:140px">Quillbase</div>
<div class="client-name" style="left:450px"><i></i>Marden</div>
<div class="client-name" style="left:764px"><i></i>Northvale</div>

<!-- News -->
<div class="band" style="top:3418px;height:537px"></div>
<div class="section-title" style="top:3503px">Latest News</div>
<div class="photo news" style="left:141px;background:linear-gradient(180deg,#9aa4ad 0%,#6f7b86 40%,#4a5561 70%,#2f3841 100%)" role="img" aria-label="Modern glass facade"><div class="news-text">New glass fit out for a city hotel lobby now complete<b>READ MORE ⟶</b></div></div>
<div class="photo news" style="left:455px;background:linear-gradient(180deg,#c9c1b5 0%,#a0968a 35%,#6d645a 70%,#3f3933 100%)" role="img" aria-label="Hotel suite interior"><div class="news-text">Suite refurbishment with solid surface desks and vanity units<b>READ MORE ⟶</b></div></div>
<div class="photo news" style="left:769px;background:linear-gradient(180deg,#6a635a 0%,#b5ab9b 35%,#7d7367 65%,#3b3631 100%)" role="img" aria-label="Hotel corridor with warm lighting"><div class="news-text">Corridor wall panels installed across four hotel floors<b>READ MORE ⟶</b></div></div>
<div class="btn-yellow" style="left:512px;top:3853px;width:173px;height:47px">VIEW ALL <svg width="30" height="10"><path d="M0 5h27M22 1l5 4-5 4" fill="none" stroke="#555" stroke-width="1.6"/></svg></div>

<!-- Map -->
<div class="photo" style="left:0;top:3968px;width:1200px;height:374px;background:linear-gradient(180deg,#e6ead9 0%,#f1efe6 30%,#e9ecdc 55%,#f3f1e8 80%,#e4e8d6 100%)" role="img" aria-label="Road map showing the office location"></div>
<svg class="abs" style="left:584px;top:4090px" width="32" height="44" viewBox="0 0 32 44"><path d="M16 2C8 2 2 8 2 16c0 11 14 26 14 26s14-15 14-26C30 8 24 2 16 2z" fill="#fff" stroke="#888" stroke-width="2"/><circle cx="16" cy="16" r="5" fill="none" stroke="#888" stroke-width="2"/></svg>

<!-- Contact -->
<div class="section-title" style="top:4434px">Contact Us</div>
<div class="contact-box" style="left:141px">
  <svg width="26" height="34" viewBox="0 0 26 34"><path d="M13 2C7 2 2 7 2 13c0 9 11 19 11 19s11-10 11-19C24 7 19 2 13 2z" fill="none" stroke="#f3e600" stroke-width="2.5"/><circle cx="13" cy="13" r="4" fill="none" stroke="#f3e600" stroke-width="2.5"/></svg>
  <h4>Address</h4><p>123 Lorem ipsum dolor sit amet</p></div>
<div class="contact-box" style="left:452px">
  <svg width="32" height="32" viewBox="0 0 32 32"><path d="M6 3l6 1 2 7-4 3c2 4 4 6 8 8l3-4 7 2 1 6c-2 3-5 4-8 3C12 26 6 20 3 12 2 9 3 5 6 3z" fill="none" stroke="#f3e600" stroke-width="2.5"/></svg>
  <h4>Call Us</h4><p>+44 (0) 1632 960 418</p></div>
<div class="contact-box" style="left:763px">
  <svg width="36" height="28" viewBox="0 0 36 28"><rect x="2" y="2" width="32" height="24" fill="none" stroke="#f3e600" stroke-width="2.5"/><path d="M2 2l16 13L34 2" fill="none" stroke="#f3e600" stroke-width="2.5"/></svg>
  <h4>Mail Us</h4><p>info@brightwellps.com</p></div>

<!-- Footer -->
<div class="abs footer">
  <span>Copyright © 2018 Brightwell Panes &amp; Stoneworks. All Rights Reserved</span>
  <span class="dots"><i></i><i></i><i></i><i></i></span>
</div>

</body>
</html>
```